Book Cover Design Project - Lesbian stories

I need a cover for my ebook of short stories. Target market is lesbians. I want something erotic (but not too over the top or porny). Something tasteful and feminine. For example two women with a flower see artist Mirel Dunstan http://www.galvoristudio.example/magazine/article.php?articleID=287.

Title: Harbour Letters, Paper Moons

By Lucinda Marvaro

```html
<!DOCTYPE html>
<html lang="en">
<head>
<meta charset="utf-8">
<title>Harbour Letters, Paper Moons — Cover</title>
<link rel="stylesheet" href="https://fonts.googleapis.com/css2?family=Alfa+Slab+One&family=Open+Sans:wght@400;700&display=swap">
<style>
  :root {
    --stage: #ebebeb;
    --cover-black: #0b0b0b;
    --title-white: #f4f2ee;
    --title-ink: #111111;
    --title-red: #8c1a22;
    --rose-red: #7a141b;
    --body-grey: #b9b9b9;
    --box-grey: #d8d8d8;
    --box-ink: #111111;
    --art-dark: #1b140e;
    --art-warm: #b04a2a;
    --art-cream: #eadcc4;
  }
  * { margin: 0; padding: 0; box-sizing: border-box; }
  html, body {
    width: 1200px; height: 800px; overflow: hidden;
    background: var(--stage);
  }
  .stage {
    position: relative; width: 1200px; height: 800px;
  }
  .cover {
    position: absolute; top: 90px; width: 420px; height: 620px;
    background: var(--cover-black); overflow: hidden;
    box-shadow: 0 10px 30px rgba(0,0,0,.25);
  }
  .cover--back { left: 150px; }
  .cover--front { left: 630px; }

  .title {
    font-family: "Alfa Slab One", Georgia, serif;
    text-align: center; line-height: .95; text-transform: uppercase;
  }
  .title__line {
    display: block; color: var(--title-white);
    -webkit-text-stroke: 1.5px var(--title-ink);
    text-shadow: 2px 2px 0 var(--title-ink);
    letter-spacing: 1px;
  }
  .title__line--accent {
    color: var(--title-red);
    -webkit-text-stroke: 1px var(--title-white);
    text-shadow: 1px 1px 0 var(--title-ink);
  }

  /* back cover */
  .back__author {
    font-family: "Alfa Slab One", Georgia, serif; color: var(--title-red);
    text-align: center; font-size: 13px; letter-spacing: .5px;
    margin-top: 14px; text-transform: uppercase;
  }
  .back__title { margin-top: 4px; position: relative; }
  .back__title .title__line { font-size: 42px; }
  .back__title .title__line--accent { font-size: 30px; }
  .rose {
    position: absolute; width: 40px; height: 40px; border-radius: 50%;
    background: radial-gradient(circle at 45% 40%, #a3262d, var(--rose-red) 70%);
  }
  .back__title .rose--left { left: 40px; bottom: 0; }
  .back__title .rose--right { right: 40px; bottom: 0; }
  .blurb {
    font-family: "Open Sans", Arial, sans-serif; color: var(--body-grey);
    font-size: 10.4px; line-height: 1.5; text-align: justify;
    padding: 16px 28px 0;
  }
  .back__boxes {
    position: absolute; left: 28px; right: 28px; bottom: 26px;
    display: flex; justify-content: space-between;
  }
  .placeholder-box {
    width: 150px; height: 46px; background: var(--box-grey);
    display: flex; align-items: center; justify-content: center;
    font-family: "Open Sans", Arial, sans-serif; font-weight: 700;
    font-size: 15px; color: var(--box-ink);
  }

  /* front cover */
  .front__art {
    position: absolute; inset: 0;
    background:
      radial-gradient(ellipse 45% 30% at 62% 18%, var(--art-warm), transparent 70%),
      radial-gradient(ellipse 45% 45% at 55% 45%, var(--art-cream), transparent 70%),
      radial-gradient(ellipse 40% 30% at 75% 70%, #d9b48a, transparent 75%),
      linear-gradient(160deg, #2a1a10, var(--art-dark) 60%, #2c2418);
  }
  .front__title { position: absolute; left: 0; right: 0; top: 395px; }
  .front__title .title__line { font-size: 48px; }
  .front__title .title__line--accent { font-size: 34px; }
  .front__title .rose--left { left: 22px; top: 120px; width: 54px; height: 54px; }
  .front__title .rose--right { right: 22px; top: 108px; width: 54px; height: 54px; }
  .front__author {
    position: absolute; left: 0; right: 0; bottom: 20px; text-align: center;
    font-family: "Alfa Slab One", Georgia, serif; font-size: 15px;
    color: var(--title-white); text-transform: uppercase; letter-spacing: .5px;
    text-shadow: 1px 1px 0 var(--title-ink);
  }
</style>
</head>
<body>
<main class="stage">
  <section class="cover cover--back" aria-label="Back cover">
    <p class="back__author">Lucinda Marvaro's</p>
    <h2 class="title back__title">
      <span class="title__line">Harbour</span>
      <span class="title__line title__line--accent">Letters</span>
      <span class="title__line">Paper</span>
      <span class="title__line title__line--accent">Moons</span>
      <span class="rose rose--left" role="img" aria-label="Red rose ornament"></span>
      <span class="rose rose--right" role="img" aria-label="Red rose ornament"></span>
    </h2>
    <p class="blurb">Lorem ipsum dolor sit amet, consectetur adipisicing elit, sed do eiusmod tempor incididunt ut labore et dolore magna aliqua. Ut enim ad minim veniam, quis nostrud exercitation. Lorem ipsum dolor sit amet, consectetur adipisicing elit, sed do eiusmod tempor incididunt ut labore et dolore magna aliqua. Ut enim ad minim veniam, quis nostrud exercitation. Lorem ipsum dolor sit amet, consectetur adipisicing elit, sed do eiusmod tempor incididunt ut labore et dolore magna aliqua. Ut enim ad minim veniam, quis nostrud exercitation. Lorem ipsum dolor sit amet, consectetur adipisicing elit, sed do eiusmod tempor incididunt ut labore et dolore magna aliqua. Ut enim ad minim veniam, quis nostrud exercitation. Lorem ipsum dolor sit amet, consectetur adipisicing elit, sed do eiusmod tempor incididunt ut labore et dolore magna aliqua. Ut enim ad minim veniam, quis nostrud exercitation. Lorem ipsum dolor sit amet, consectetur adipisicing elit, sed do eiusmod tempor incididunt ut labore et dolore magna aliqua. Ut enim ad minim veniam, quis nostrud exercitation.</p>
    <div class="back__boxes">
      <div class="placeholder-box">LOGO</div>
      <div class="placeholder-box">ISBN</div>
    </div>
  </section>

  <section class="cover cover--front" aria-label="Front cover">
    <div class="front__art" role="img" aria-label="Painted illustration of two women embracing, one with red hair, in warm cream and dark tones"></div>
    <h1 class="title front__title">
      <span class="title__line">Harbour</span>
      <span class="title__line title__line--accent">Letters</span>
      <span class="title__line">Paper</span>
      <span class="title__line title__line--accent">Moons</span>
      <span class="rose rose--left" role="img" aria-label="Red rose ornament"></span>
      <span class="rose rose--right" role="img" aria-label="Red rose ornament"></span>
    </h1>
    <p class="front__author">By Lucinda Marvaro</p>
  </section>
</main>
</body>
</html>
```